Medical software helping patients with dry eye disease needs a business card

We have a logo we just need a design for a business card for a Canadian company called LUMA: Dry Eye. We use AI technology to assist optometrists in properly diagnosing patients with dry eye disease reducing wait times in doctors offices and accuracy of diagnosis as well as identifying key possible indicators and tailored treatment plans. The final design should be clean and medical looking. Our mission is to help patients and our logo using blues and whites.

```html
<!DOCTYPE html>
<html lang="en">
<head>
<meta charset="utf-8">
<title>LUMA: Dry Eye — Business Card</title>
<link rel="stylesheet" href="https://fonts.googleapis.com/css2?family=Montserrat:wght@800&family=Lato:wght@400&family=Roboto:wght@400&display=swap">
<style>
  :root {
    --backdrop: #1b1b1b;
    --kraft-light: #e0c196;
    --kraft-mid: #c49a68;
    --kraft-dark: #a87a4a;
    --ink: #0d0a07;
  }
  * { margin: 0; padding: 0; box-sizing: border-box; }
  html, body {
    width: 1093px;
    height: 1200px;
    overflow: hidden;
    background: var(--backdrop);
  }
  .canvas {
    position: relative;
    width: 1093px;
    height: 1200px;
  }
  .card {
    position: absolute;
    left: 265px;
    width: 580px;
    height: 357px;
    background: linear-gradient(135deg, var(--kraft-light) 0%, var(--kraft-mid) 55%, var(--kraft-dark) 100%);
    color: var(--ink);
    text-align: center;
  }
  .card--front { top: 226px; }
  .card--back { top: 620px; }

  .contact {
    position: absolute;
    top: 70px;
    left: 0;
    right: 0;
    font-family: 'Lato', sans-serif;
    font-size: 17.5px;
    line-height: 21px;
    white-space: nowrap;
  }
  .contact__name {
    font-family: 'Montserrat', sans-serif;
    font-weight: 800;
    font-size: 20px;
    line-height: 22px;
    letter-spacing: 0.2px;
  }
  .contact__role {
    font-family: 'Roboto', sans-serif;
    font-size: 16.5px;
    line-height: 18px;
  }
  .contact__rule {
    width: 94px;
    height: 1px;
    background: var(--ink);
    margin: 15px auto 16px;
  }
  .contact__rule--lower { margin-top: 17px; margin-bottom: 19px; }

  .brand {
    position: absolute;
    top: 150px;
    left: 0;
    right: 0;
    display: flex;
    align-items: center;
    justify-content: center;
    gap: 18px;
  }
  .brand__dot {
    width: 48px;
    height: 48px;
    border-radius: 50%;
    background: var(--ink);
  }
  .brand__name {
    font-family: 'Montserrat', sans-serif;
    font-weight: 800;
    font-size: 44px;
    line-height: 1;
    letter-spacing: -0.5px;
  }
</style>
</head>
<body>
<main class="canvas">
  <section class="card card--front" aria-label="Business card front">
    <div class="contact">
      <p class="contact__name">MARCUS ELLERY</p>
      <p class="contact__role">Managing Director</p>
      <div class="contact__rule"></div>
      <p>M: 044-987 650 312</p>
      <p>E: hello@lumamail.com</p>
      <p>W: www.lumaclinic.com</p>
      <div class="contact__rule contact__rule--lower"></div>
      <p>48210, Harbour Line Road</p>
      <p>Northvale City, 654321.</p>
    </div>
  </section>

  <section class="card card--back" aria-label="Business card back">
    <div class="brand">
      <span class="brand__dot"></span>
      <span class="brand__name">LUMA: Dry Eye</span>
    </div>
  </section>
</main>
</body>
</html>
```